Business Card Design Project

We need a business card design for a management consultancy focused on financial innovation and digital money, run by experts from the Financial Services, Telecoms and Money Transfer industries.
Our products include services such as Mobile Payments, Mobile Money, Digital Wallets, Online Payments, Branchless Banking and more. We work with regulatory information, business plans, financial modelling, strategic planning, new products functional specification, new technologies evaluation, etc.
See company logo attached.
We would like to see 2 versions: one in portuguese and one in english (regarding data information). You can see below information needed (whenever there is a difference between the two versions, the first one is in english and the second one in portuguese).

Name
Position
Phone/ Tel: ++55-11-xxxx-xxxx
Cell/ Cel: ++55-11-9 xxxx-xxxx
Dr. Tavares Lobato Av., 318 - Tower II - 16th floor / Avenida Dr. Tavares Lobato, 318 - Torre II - 16o. andar
São Paulo - SP
01327-118 - Brazil/ 01327-118 - Brasil

Target Market(s)

Audience: C-level executives from banks, credit card companies, acquirers, IT developers, retailers

Industry/Entity Type

Financial

Requirements
Must have
• Must use the logo and information above. Front must have white background. Back side should have only logo.
Nice to have
• Back should be in another colour but if it seems too exxagerated, maintain back in white also.
Should not have
• Do not add other illustrations to the business card.

```html
<!DOCTYPE html>
<html lang="en">
<head>
<meta charset="utf-8">
<title>Veridian Consulting – Business Cards</title>
<link href="https://fonts.googleapis.com/css2?family=Cormorant+Garamond:wght@400;500;600&display=swap" rel="stylesheet">
<style>
  :root {
    --page-bg: #e9e7e3;
    --card-white: #ffffff;
    --ink-navy: #1f3a78;
    --blue-light: #3f8fd6;
    --blue-mid: #2f5f9c;
    --blue-deep: #1a2a66;
    --blue-night: #0f1748;
    --text-light: #e8eef8;
    --card-shadow: rgba(0, 0, 0, 0.18);
  }
  * { box-sizing: border-box; margin: 0; padding: 0; }
  html, body {
    width: 1200px;
    height: 967px;
    overflow: hidden;
    background: var(--page-bg);
    font-family: "Cormorant Garamond", Georgia, serif;
  }
  .canvas {
    position: relative;
    width: 1200px;
    height: 967px;
  }
  .card {
    position: absolute;
    top: 160px;
    width: 380px;
    height: 640px;
    background: var(--card-white);
    box-shadow: 0 6px 22px var(--card-shadow);
    overflow: hidden;
  }
  .card--front { left: 190px; }
  .card--back { left: 630px; }

  .brand {
    display: flex;
    align-items: center;
    gap: 10px;
    max-width: 100%;
  }
  .brand__mark {
    width: 20px;
    height: 20px;
    background: var(--ink-navy);
    flex: none;
  }
  .brand__name {
    font-weight: 600;
    font-size: 21px;
    letter-spacing: 0.06em;
    text-transform: uppercase;
    color: var(--ink-navy);
    white-space: nowrap;
  }

  /* Front */
  .front__header {
    height: 118px;
    display: flex;
    align-items: center;
    padding: 0 34px;
  }
  .front__panel {
    position: absolute;
    top: 118px;
    left: 0;
    right: 0;
    bottom: 0;
    background:
      radial-gradient(ellipse 90% 40% at 30% 0%, rgba(120, 190, 245, 0.55), rgba(120, 190, 245, 0) 70%),
      linear-gradient(160deg, var(--blue-light) 0%, var(--blue-mid) 30%, var(--blue-deep) 70%, var(--blue-night) 100%);
  }
  .holder {
    position: absolute;
    top: 70px;
    left: 0;
    right: 0;
    text-align: center;
    color: var(--text-light);
  }
  .holder__name {
    font-weight: 500;
    font-size: 28px;
    letter-spacing: 0.08em;
    text-transform: uppercase;
  }
  .holder__role {
    margin-top: 6px;
    font-size: 17px;
    letter-spacing: 0.04em;
  }
  .contact {
    position: absolute;
    left: 34px;
    right: 24px;
    bottom: 40px;
    padding-left: 12px;
    border-left: 1px solid rgba(232, 238, 248, 0.7);
    color: var(--text-light);
    font-size: 14px;
    line-height: 1.45;
    list-style: none;
  }
  .contact li { white-space: nowrap; }

  /* Back */
  .back__logo {
    position: absolute;
    top: 300px;
    left: 30px;
    right: 30px;
    display: flex;
    justify-content: center;
  }
</style>
</head>
<body>
  <main class="canvas">
    <section class="card card--front" aria-label="Business card front">
      <header class="front__header">
        <div class="brand">
          <span class="brand__mark"></span>
          <span class="brand__name">Veridian Consulting</span>
        </div>
      </header>
      <div class="front__panel" role="img" aria-label="Blue gradient background with a light speckled texture">
        <div class="holder">
          <p class="holder__name">Paulo Mendes</p>
          <p class="holder__role">consultant</p>
        </div>
        <ul class="contact">
          <li>Phone/ Tel: ++55-11-xxxx-xxxx</li>
          <li>Cell/ Cel: ++55-11-9 xxxx-xxxx</li>
          <li>Dr. Tavares Lobato Av., 318 - Tower II - 16th floor</li>
          <li>São Paulo - SP</li>
          <li>01327-118 - Brazil/ 01327-118 - Brasil</li>
        </ul>
      </div>
    </section>

    <section class="card card--back" aria-label="Business card back">
      <div class="back__logo">
        <div class="brand">
          <span class="brand__mark"></span>
          <span class="brand__name">Veridian Consulting</span>
        </div>
      </div>
    </section>
  </main>
</body>
</html>
```